Crestline Supply Software Design

I would like a construction focused flyer design (if possible, inline with the current design esthetic from my website www.crsupsw.com), 1 standard US page (8.5x11"), front and back, full color glossy. I want a design I can use for multiple software partners, so I want the ability to edit the template that is created. This can be full page or folded- whatever you think is best.Attached are my logos, and a current flyer. I want to use the logo and the color scheme- feel free to make the logo colors even brighter. Everything else can be changed! Any additional graphics should be software or construction focused.

Target Market(s)

Electrical, Mechanical and Plumbing Construction Companies, specifically their accounting, IT, purchasing staff.

Font styles to use
Sans Serif

Colors
6b449b
9ccb3b

Requirements
Must have
• Lots of construction oriented graphics. Discreet boxes for text that can be changed in using photoshop or Illustrator products CS6 or earlier.
• Designs should be:
• - B2B focused
• - merge technology and construction
• - Show how technology can save time
• - Automation is a good thing
Should not have
• Be saved in a format that can not be used by CS6 or earlier.

```html
<!DOCTYPE html>
<html lang="en">
<head>
<meta charset="utf-8">
<title>Crestline Supply Software Flyer</title>
<link href="https://fonts.googleapis.com/css2?family=Ubuntu:wght@700&family=Roboto+Condensed:wght@300;400&display=swap" rel="stylesheet">
<style>
:root{
  --purple:#6b449b;
  --purple-band:#6a4ba0;
  --green:#3db54a;
  --green-text:#3aaa35;
  --green-dark:#1f6b3c;
  --ink:#4a4a4a;
  --white:#ffffff;
  --bg:#e6e7e8;
}
*{box-sizing:border-box;margin:0;padding:0}
html,body{width:1200px;height:810px;overflow:hidden;background:var(--bg)}
body{position:relative;font-family:"Roboto Condensed",sans-serif;font-weight:300;color:var(--ink)}
.page{position:absolute;top:80px;width:502px;height:650px;background:var(--white);overflow:hidden;box-shadow:0 4px 10px rgba(0,0,0,.25)}
.page--front{left:76px}
.page--back{left:622px}
.abs{position:absolute}

/* front */
.hero-photo{left:0;top:0;width:502px;height:251px;background:linear-gradient(135deg,#5b5570 0%,#3f3a52 45%,#56506a 100%)}
.hero-panel{left:0;top:0;width:261px;height:251px;background:linear-gradient(180deg,rgba(30,110,60,.9),rgba(40,140,70,.85))}
.hero-title{left:36px;top:34px;font-family:"Ubuntu",sans-serif;font-weight:700;color:var(--white);line-height:1}
.hero-title span{display:block}
.hero-title .t1{font-size:36px;margin-bottom:6px}
.hero-title .t2{font-size:27px;margin-bottom:4px}
.hero-title .t3{font-size:37px}
.hero-roof{left:0;top:0}
.promo-band{left:0;top:251px;width:502px;height:33px;background:var(--purple-band);color:var(--white);font-size:13px;font-weight:400;display:flex;align-items:center;justify-content:center}
.section-title{left:0;width:502px;text-align:center;color:var(--purple);font-weight:300}
.title-main{top:299px;font-size:21px}
.title-rule{left:48px;top:328px;width:406px;height:2px;background:var(--purple)}
.title-sub{top:332px;font-size:15px}
.feature{width:220px;text-align:center;color:var(--green-text);font-size:11px;line-height:14px;font-weight:400}
.feature b{display:block;font-weight:400}
.icon-circle{width:58px;height:58px;border-radius:50%;background:var(--purple);display:flex;align-items:center;justify-content:center}
.about{left:0;top:561px;width:502px;height:89px;background:var(--green);color:var(--white);text-align:center}
.about h2{font-weight:300;font-size:16px;margin-top:14px}
.about-rule{width:310px;height:1px;background:var(--white);margin:3px auto 6px}
.about p{font-size:8.6px;line-height:12px;padding:0 36px}

/* back */
.products-title{left:30px;top:40px;color:var(--purple);font-size:26px;font-weight:300}
.products-intro{left:30px;top:72px;width:272px;font-size:10.4px;line-height:14px;color:#333}
.devices{left:313px;top:28px;width:157px;height:140px;background:linear-gradient(160deg,#3a3a3a,#6d6d6d 60%,#2b2b2b)}
.product{width:215px}
.product h3{font-weight:300;font-size:16px;color:#222;display:flex;align-items:center;gap:10px;line-height:20px}
.product p{font-size:8.8px;line-height:12px;color:#333;margin-top:4px}
.product svg{flex:none}
.band{left:0;top:325px;width:502px;height:207px;background:var(--purple-band);color:var(--white)}
.band-icon{width:70px;height:70px;border-radius:50%;border:2px solid var(--white);display:flex;align-items:center;justify-content:center}
.band-col{top:90px}
.band-col h4{font-weight:300;font-size:13px;margin-bottom:4px}
.band-col ul{list-style:none;font-size:9px;line-height:11.8px}
.band-col li{padding-left:7px;text-indent:-7px}
.band-col li::before{content:"\2022 "}
.brand-square{left:36px;top:548px;width:56px;height:56px;background:#111}
.brand-name{left:30px;top:608px;width:70px;text-align:center;font-size:7.5px;line-height:9px;font-weight:400;color:#111;letter-spacing:.5px}
.contact{left:114px;top:558px;color:#333}
.contact .phone{font-size:21px;line-height:26px}
.contact .line{font-size:14px;line-height:18px;font-weight:400}
.social-wedge{left:0;top:0}
.social{width:32px;height:32px;border-radius:50%;border:2px solid var(--white);top:598px}
</style>
</head>
<body>

<section class="page page--front">
  <div class="abs hero-photo" role="img" aria-label="Photo of a team meeting in a modern brick-walled office"></div>
  <div class="abs hero-panel"></div>
  <h1 class="abs hero-title"><span class="t1">CRESTLINE</span><span class="t2">SUPPLY</span><span class="t3">SOFTWARE</span></h1>
  <svg class="abs hero-roof" width="502" height="251" viewBox="0 0 502 251"><polyline points="18,210 138,166 261,210" fill="none" stroke="#fff" stroke-width="4"/></svg>
  <div class="abs promo-band">REJOICE! Purchase Order Creation and Vendor Automation PLUS Invoice Matching!</div>

  <h2 class="abs section-title title-main">TAKING PRODUCTIVITY TO THE NEXT LEVEL</h2>
  <div class="abs title-rule"></div>
  <p class="abs section-title title-sub">Swift Purchase - Swift Order - Swift Invoice</p>

  <div class="abs feature" style="left:38px;top:357px">
    <div class="icon-circle" style="margin:0 auto 10px"><svg width="28" height="24" viewBox="0 0 28 24"><path d="M3 2h16v10a6 6 0 0 1-6 6H9a6 6 0 0 1-6-6z" fill="#fff"/><path d="M19 5h3a3.5 3.5 0 0 1 0 7h-3" fill="none" stroke="#fff" stroke-width="2.5"/><rect x="0" y="20" width="24" height="3" fill="#fff"/></svg></div>
    <b>IT'S EASY</b>Easily write terrific looking PO's
  </div>
  <div class="abs feature" style="left:256px;top:357px">
    <div class="icon-circle" style="margin:0 auto 12px"><svg width="28" height="26" viewBox="0 0 28 26"><path d="M27 1L1 12l8 3 2 9 4-6 7 4z" fill="#fff"/><path d="M9 15L27 1 13 18" fill="none" stroke="#6b449b" stroke-width="1.5"/></svg></div>
    <b>IT'S A SNAP</b>Create material quote requests in a snap
  </div>
  <div class="abs feature" style="left:37px;top:456px">
    <div class="icon-circle" style="margin:0 auto 14px"><span style="color:#fff;font-size:30px;font-weight:400">$</span></div>
    <b>E-COMMERCE</b>Use the power of automation and data
  </div>
  <div class="abs feature" style="left:256px;top:458px">
    <div class="icon-circle" style="margin:0 auto 12px"><svg width="28" height="26" viewBox="0 0 28 26"><rect x="1" y="11" width="6" height="14" fill="#fff"/><path d="M9 11l5-10c3 0 4 2 3 5l-1 4h8a2.5 2.5 0 0 1 0 5h-1a2.5 2.5 0 0 1 0 5h-1a2.5 2.5 0 0 1-1 5H9z" fill="#fff"/></svg></div>
    <b>NEVER WASTE TIME</b>Automated matching of PO to Invoice
  </div>

  <div class="abs about">
    <h2>ABOUT US</h2>
    <div class="about-rule"></div>
    <p>Crestline Supply Software makes the electronic exchange of purchase information seamless, accurate, and cost effective for clients and vendors while providing growth opportunities for our employees.</p>
  </div>
</section>

<section class="page page--back">
  <h2 class="abs products-title">OUR PRODUCTS</h2>
  <p class="abs products-intro">With over 25 years in the construction industry, we understand the frustration of inefficient procurement processes, the financial pains and ramifications of setbacks, and the need for consistently flawless execution of purchasing tasks. With an industry average of less than 6% profit per project, we know what's on the line.</p>
  <div class="abs devices" role="img" aria-label="Software screens shown on a desktop monitor, tablet and phone"></div>

  <div class="abs product" style="left:30px;top:183px">
    <h3><span style="color:var(--purple);font-size:24px;font-weight:400;width:18px">$</span>SWIFT PURCHASE</h3>
    <p>Swift Purchase is a comprehensive, easy-to-use software package for material management.</p>
  </div>
  <div class="abs product" style="left:30px;top:238px">
    <h3><svg width="20" height="14" viewBox="0 0 20 14"><path d="M2 13a8 8 0 0 1 16 0" fill="none" stroke="#6b449b" stroke-width="2.5"/><path d="M10 13l4-7" stroke="#6b449b" stroke-width="2"/></svg>SWIFT ORDER</h3>
    <p>Swift Order Confirmation uses the latest technology to harness all of the information your vendor has about your order and then makes that information available to you.</p>
  </div>
  <div class="abs product" style="left:257px;top:183px">
    <h3><svg width="20" height="18" viewBox="0 0 28 26"><path d="M27 1L1 12l8 3 2 9 4-6 7 4z" fill="#6b449b"/></svg>SWIFT INVOICE</h3>
    <p>Tired of trying to match invoice items to order items? Swift Invoice builds on what Swift Order Confirmation started.</p>
  </div>
  <div class="abs product" style="left:257px;top:248px">
    <h3><svg width="20" height="20" viewBox="0 0 20 20"><path d="M2 18l9-9" stroke="#6b449b" stroke-width="3.5" stroke-linecap="round"/><path d="M17 3a5 5 0 0 0-6 6l3 0 0-3z" fill="#6b449b"/><circle cx="14" cy="6" r="5" fill="none" stroke="#6b449b" stroke-width="2.5" stroke-dasharray="22 10"/></svg>GEAR TRACKER</h3>
    <p>Gear Tracker follows the Swift Purchase design, which incorporates ease of use with an intuitive, user friendly interface.</p>
  </div>

  <div class="abs band">
    <div class="abs band-icon" style="left:57px;top:8px"><svg width="36" height="32" viewBox="0 0 36 32"><rect x="0" y="0" width="36" height="8" rx="1" fill="#fff"/><rect x="0" y="12" width="36" height="8" rx="1" fill="#fff"/><rect x="0" y="24" width="36" height="8" rx="1" fill="#fff"/></svg></div>
    <div class="abs band-icon" style="left:214px;top:8px"><svg width="40" height="30" viewBox="0 0 40 30"><circle cx="20" cy="7" r="6" fill="#fff"/><circle cx="8" cy="10" r="4.5" fill="#fff"/><circle cx="32" cy="10" r="4.5" fill="#fff"/><path d="M10 30v-6a10 10 0 0 1 20 0v6z" fill="#fff"/><path d="M0 28v-4a8 8 0 0 1 12-6v10z" fill="#fff"/><path d="M40 28v-4a8 8 0 0 0-12-6v10z" fill="#fff"/></svg></div>
    <div class="abs band-icon" style="left:379px;top:8px"><svg width="32" height="36" viewBox="0 0 32 36"><ellipse cx="16" cy="5" rx="16" ry="5" fill="#fff"/><path d="M0 9c0 3 7 5 16 5s16-2 16-5v7c0 3-7 5-16 5S0 19 0 16z" fill="#fff"/><path d="M0 20c0 3 7 5 16 5s16-2 16-5v10c0 3-7 5-16 5S0 33 0 30z" fill="#fff"/></svg></div>

    <div class="abs band-col" style="left:30px;width:135px">
      <h4>SWIFT PURCHASE</h4>
      <ul><li>Swiftly create professional -looking POs</li><li>Track orders to jobsites</li><li>Review cumulated jobsite material usage</li><li>Link to your accounting system</li></ul>
    </div>
    <div class="abs band-col" style="left:173px;width:165px">
      <h4>SWIFT ORDER CONFIRMATION</h4>
      <ul style="width:120px"><li>Create POs of any size in less than a minute</li><li>Quickly get material orders to your vendors</li><li>No new software is needed for your vendors</li><li>Spend more time managing important materials</li></ul>
    </div>
    <div class="abs band-col" style="left:349px;width:135px">
      <h4>SWIFT INVOICE</h4>
      <ul><li>Receive your invoices and Invoice Images daily</li><li>Automatically matches invoice lines to PO lines</li><li>Imports Invoice Images into your Imaging system</li><li>Integrates with your Accounting system</li></ul>
    </div>
  </div>

  <div class="abs brand-square"></div>
  <div class="abs brand-name">CRESTLINE SUPPLY SOFTWARE</div>
  <div class="abs contact">
    <div class="phone">Phone (800) 555-0142</div>
    <div class="line">Crestline Supply Software, Inc.</div>
    <div class="line">PO Box 4021, Riverton, TX&nbsp; 78001</div>
  </div>
  <svg class="abs social-wedge" width="502" height="650" viewBox="0 0 502 650"><polygon points="323,636 358,586 502,586 502,636" fill="var(--green)"/><rect x="0" y="637" width="502" height="5" fill="var(--green)"/></svg>
  <div class="abs social" style="left:374px"></div>
  <div class="abs social" style="left:410px"></div>
  <div class="abs social" style="left:445px"></div>
</section>

</body>
</html>
```